New homepage and Product page - Verdant Qa

Reason: I have narrowed it done to 3 designers and just need to get the designs revised

Industry/Entity Type

Product

```html
<!DOCTYPE html>
<html lang="en">
<head>
<meta charset="utf-8">
<title>Verdant Qa – Home</title>
<link href="https://fonts.googleapis.com/css2?family=Figtree:wght@300;400;600;700&display=swap" rel="stylesheet">
<style>
:root{
  --green-light:#74bd22;
  --green-mid:#5ea512;
  --green-dark:#4a8a0c;
  --green-head:#4b8a1a;
  --green-link:#6aab1c;
  --orange:#f08a24;
  --text:#666;
  --text-strong:#5c5c5c;
  --panel:#ecebe5;
  --border:#dcdcd6;
  --footer:#e9e6e1;
  --rule:#cfccc6;
  --badge-brown:#5e5650;
  --gold:#e0a21c;
  --social:#a9a6a1;
}
*{box-sizing:border-box;margin:0;padding:0}
html,body{width:1200px;height:1000px;overflow:hidden;background:#fff;font-family:"Figtree",Arial,sans-serif;color:var(--text)}
.page{position:relative;width:1200px;height:1000px}
.abs{position:absolute}

.hero{left:0;top:0;width:1200px;height:250px;background:linear-gradient(180deg,var(--green-light),var(--green-mid) 60%,#4f9a0c);overflow:hidden}
.hero-arrow{top:0;width:50px;height:20px;background:#8cc63f;border-radius:0 0 4px 4px}
.hero-arrow.prev{left:0;border-radius:0 0 4px 0}
.hero-arrow.next{right:0;border-radius:0 0 0 4px}
.hero-copy{left:119px;top:2px;width:450px;color:#fff;font-weight:600;font-size:18px;line-height:23.5px}
.btn-learn{left:120px;top:113px;width:176px;height:50px;background:var(--orange);border:3px solid #fff;border-radius:3px;color:#fff;font-size:20px;line-height:44px;padding-left:15px}
.btn-learn span{color:#c84a10;margin-left:10px;font-weight:700}
.hero-tagline{left:315px;top:115px;width:345px;height:50px;background:linear-gradient(90deg,rgba(200,240,120,.35),rgba(200,240,120,.15));border-radius:6px}
.hero-fruit{left:595px;top:0;width:175px;height:210px;background:radial-gradient(ellipse at 60% 40%,#eef3d6,#b9cf7a 70%,rgba(120,170,40,0) 100%)}
.hero-product{left:768px;top:0;width:284px;height:198px;background:linear-gradient(180deg,#f7d63a 0 22%,#fff 22% 30%,#f4a640 30% 78%,#fff 78%);border-radius:0 0 4px 4px;box-shadow:0 4px 10px rgba(0,0,0,.2)}
.hero-curve{left:0;top:228px}
.dots{left:573px;top:243px;display:flex;gap:6px}
.dots i{width:14px;height:5px;border-radius:3px;background:#ddd}
.dots i.on{background:var(--green-mid)}

.intro-title{left:0;top:298px;width:1200px;text-align:center;font-weight:300;font-size:42px;color:var(--green-head);letter-spacing:.5px}
.intro-text{left:180px;top:352px;width:840px;text-align:center;font-size:21px;line-height:30px;color:var(--text)}

.features{left:120px;top:460px;width:630px;height:270px;border:1px solid var(--border);background:linear-gradient(180deg,#e6e6de,#fff 80%)}
.features-head{position:absolute;left:-1px;top:-1px;width:630px;height:40px;background:var(--green-dark);color:#fff;font-size:22px;line-height:42px;padding-left:23px}
.feature{position:absolute;left:22px;width:590px}
.feature svg{position:absolute;left:0;top:2px}
.feature h3{margin-left:31px;font-size:19px;font-weight:600;color:var(--text-strong);text-transform:uppercase;line-height:24px}
.feature p{margin-left:32px;font-size:15.5px;line-height:22px;color:var(--text)}

.guarantee{left:780px;top:460px;width:300px;height:270px;background:var(--panel)}
.guarantee-leaves{position:absolute;left:0;top:0;width:168px;height:136px;background:radial-gradient(ellipse at 40% 50%,#8cc63f,#c6dda0 70%,rgba(236,235,229,0));}
.guarantee-seal{position:absolute;left:162px;top:18px;width:110px;height:110px;border-radius:50%;background:radial-gradient(circle at 45% 40%,#ffd25a,var(--gold) 70%,#b97a10)}
.guarantee-text{position:absolute;left:33px;top:140px;width:240px;font-size:15.5px;line-height:22px}
.guarantee-text b{color:var(--text-strong);font-weight:600}

.trust-item{top:767px}
.trust-badge{left:119px;top:767px;width:70px;height:70px;border-radius:50%;background:var(--badge-brown)}
.trust-copy{left:206px;top:772px;width:380px;font-size:14px;line-height:20px}
.trust-copy a{color:var(--green-link);font-weight:700;text-decoration:none}
.usa-shield{left:620px;top:772px}
.usa-copy{left:703px;top:769px;width:360px;font-size:14px;line-height:21px}
.usa-copy b{display:block;font-size:15px;font-weight:600;color:var(--text-strong)}

.footer{left:0;top:871px;width:1200px;height:129px;background:var(--footer);border-top:1px solid var(--rule)}
.copyright{position:absolute;left:120px;top:29px;font-size:12px;color:#777}
.footer-nav{position:absolute;left:764px;top:35px;font-size:13px;color:#999}
.footer-nav a{color:var(--green-link);text-decoration:none}
.footer-nav span{margin:0 6px}
.social{position:absolute;left:970px;top:28px;display:flex;gap:10px}
.social i{display:block;width:30px;height:30px;background:var(--social)}
</style>
</head>
<body>
<div class="page">

  <section class="hero abs">
    <div class="hero-arrow prev abs"></div>
    <div class="hero-arrow next abs"></div>
    <p class="hero-copy abs">Verdant Garcinia Blend is made with premium garcinia cambogia that supplies 60% HCA, which is the active weight-loss component of garcinia cambogia.</p>
    <div class="btn-learn abs">LEARN MORE<span>❯</span></div>
    <div class="hero-tagline abs" role="img" aria-label="Hand-lettered slogan: Start Losing Weight Today!"></div>
    <div class="hero-fruit abs" role="img" aria-label="Photo of sliced garcinia fruit"></div>
    <div class="hero-product abs" role="img" aria-label="Photo of the two-bottle bonus pack box"></div>
    <svg class="hero-curve abs" width="1200" height="22" viewBox="0 0 1200 22">
      <path d="M0 22 L510 22 C545 22 545 7 580 7 L620 7 C655 7 655 22 690 22 L1200 22 Z" fill="#fff"/>
    </svg>
    <div class="dots abs"><i class="on"></i><i></i><i></i></div>
  </section>

  <h1 class="intro-title abs">THE BEST OF NATURE &amp; SCIENCE</h1>
  <p class="intro-text abs">New Verdant Qa is line of natural, high-quality, weight-loss supplements that are scientifically formulated for better efficiency!</p>

  <section class="features abs">
    <h2 class="features-head">ALL OUR PRODUCTS ARE</h2>
    <div class="feature" style="top:62px">
      <svg width="24" height="26" viewBox="0 0 24 26"><path d="M2 24 C2 10 10 3 23 2 C22 14 15 22 2 24 Z" fill="#7cbf2a"/><path d="M3 23 L18 7" stroke="#fff" stroke-width="1.5"/></svg>
      <h3>100% Pure Natural Ingredients</h3>
      <p>Verdant Qa products are made with 100% pure natural ingredients. Unlike other products, Verdant Qa products are made with premium natural ingredients for effective results.</p>
    </div>
    <div class="feature" style="top:172px">
      <svg width="24" height="26" viewBox="0 0 24 26"><path d="M2 24 C2 10 10 3 23 2 C22 14 15 22 2 24 Z" fill="#7cbf2a"/><path d="M3 23 L18 7" stroke="#fff" stroke-width="1.5"/></svg>
      <h3>Scientifically Formulated</h3>
      <p>Verdant Qa products are scientifically formulated to deliver the exact clinically tested doses that are needed to see results!</p>
    </div>
  </section>

  <aside class="guarantee abs">
    <div class="guarantee-leaves" role="img" aria-label="Illustration of a green leafy branch"></div>
    <div class="guarantee-seal" role="img" aria-label="Money back guarantee seal"></div>
    <p class="guarantee-text"><b>Verdant Qa is guaranteed to work or your money back.</b> Simply return it to the place of purchase within 30 days for a refund with original receipt.</p>
  </aside>

  <div class="trust-badge abs" role="img" aria-label="Clinically tested dose badge"></div>
  <p class="trust-copy abs">Lorem ipsum dolor sit amet, consectetur adipisicing elit, sed do eiusmod incididunt ut labore et dolore magna aliqua enim ad minim laboris nisi ut aliquip ext ... <a href="#">Find out more</a></p>

  <svg class="usa-shield abs" width="68" height="66" viewBox="0 0 68 66" role="img" aria-label="Made in the USA shield badge">
    <path d="M4 2 H64 V34 C64 50 50 60 34 65 C18 60 4 50 4 34 Z" fill="#9a9895"/>
  </svg>
  <p class="usa-copy abs"><b>Made in the USA</b>Verdant Qa is manufactured in a GMP-compliant manufacturing facility to ensure 100% quality.</p>

  <footer class="footer abs">
    <p class="copyright">© Copyright 2014 Verdant Qa</p>
    <nav class="footer-nav"><a href="#">Home</a><span>|</span><a href="#">Products</a><span>|</span><a href="#">Contact Us</a></nav>
    <div class="social" aria-label="Social links"><i></i><i></i><i></i></div>
  </footer>

</div>
</body>
</html>
```